Flyer for Harbourline Accounting & Taxation, a local tax practice

Flyer for my business to be distributed locally in the Western Suburb of Melbourne (Size: DL, Fold: Flat, Backside: Blank) This will include below information (Font, color and capitalization of the text is for the designer's creativity):
Harbourline Accounting & Taxation Your Local Tax Accountant
ABN: 37 481 259 604
Address: 9 Marlo Place, Wattle Bend
kolvend@hbatx.com.au
Call Tobias on 0419 786 205 to book your appointment
Services we offer:
Individual & Company Tax Returns
Company & Trust formation
Business Advisory
Bookkeeping
BAS & IAS
Payroll
TPAR
Please include the logo of the business attached which was designed by PixelForum few years ago.
Please include the NBF, RCQ and Lumo logos somewhere in the bottom, preferable the same size and aligned (attached)

```html
<!DOCTYPE html>
<html lang="en">
<head>
<meta charset="utf-8">
<title>Harbourline Accounting &amp; Taxation – Flyer</title>
<link href="https://fonts.googleapis.com/css2?family=Montserrat:wght@400;500;700&family=Lato:wght@400;700&display=swap" rel="stylesheet">
<style>
  :root{
    --orange:#e8773a;
    --charcoal:#46484b;
    --ink:#3d3f42;
    --white:#ffffff;
    --backdrop:#dcdcdc;
  }
  *{margin:0;padding:0;box-sizing:border-box;}
  html,body{width:732px;height:1200px;overflow:hidden;background:var(--backdrop);}
  .flyer{
    position:absolute;left:97px;top:30px;width:537px;height:1140px;
    background:var(--white);overflow:hidden;
    font-family:"Montserrat",Arial,sans-serif;color:var(--ink);
  }
  .hero-photo{
    position:absolute;left:0;top:0;width:537px;height:562px;
    background:linear-gradient(180deg,#2a2f38 0%,#3a3f48 35%,#8b8580 62%,#cfd3d2 80%,#e3e6e4 100%);
  }
  .brand-header{
    position:absolute;left:0;top:0;width:335px;height:105px;
    background:var(--white);border-bottom-right-radius:70px;
  }
  .brand-mark{position:absolute;left:38px;top:34px;width:14px;height:14px;background:var(--orange);}
  .brand-name{
    position:absolute;left:60px;top:28px;width:240px;
    font-size:16px;font-weight:700;line-height:22px;color:var(--charcoal);
  }
  .headline-panel{position:absolute;left:0;top:441px;width:400px;height:121px;}
  .headline{
    position:absolute;left:24px;top:450px;
    font-size:24px;line-height:36px;color:var(--white);font-weight:400;
  }
  .headline .accent{color:var(--orange);font-weight:700;}
  .services-title{
    position:absolute;left:32px;top:587px;font-size:34px;font-weight:400;color:var(--ink);letter-spacing:-0.3px;
  }
  .services-title strong{color:var(--orange);font-weight:700;}
  .title-rule{position:absolute;left:32px;top:641px;width:212px;height:3px;background:var(--ink);}
  .service{position:absolute;display:flex;align-items:center;height:40px;}
  .service-icon{width:40px;height:40px;background:var(--orange);display:flex;align-items:center;justify-content:center;flex:none;}
  .service-icon svg{width:26px;height:26px;}
  .service-label{font-size:20px;color:var(--ink);white-space:nowrap;}
  .contact-band{
    position:absolute;left:0;top:914px;width:537px;height:51px;background:var(--charcoal);
    font-family:"Lato",Arial,sans-serif;font-size:15px;color:var(--white);
  }
  .contact-item{position:absolute;top:13px;display:flex;align-items:center;gap:9px;}
  .contact-icon{width:22px;height:22px;background:var(--orange);display:flex;align-items:center;justify-content:center;}
  .abn-band{
    position:absolute;left:0;top:965px;width:537px;height:54px;background:var(--orange);
    display:flex;align-items:center;gap:10px;
    font-family:"Lato",Arial,sans-serif;font-size:16px;color:var(--white);
  }
  .abn-band .rule{flex:1;height:2px;background:var(--white);}
  .abn-band b{font-weight:700;}
  .call-icon{position:absolute;left:56px;top:1030px;width:86px;height:86px;}
  .call-lead{position:absolute;left:165px;top:1033px;font-size:17px;font-weight:500;color:var(--ink);}
  .call-number{
    position:absolute;left:154px;top:1052px;font-size:47px;font-weight:700;color:var(--orange);letter-spacing:-1px;
  }
</style>
</head>
<body>
<main class="flyer">
  <div class="hero-photo" role="img" aria-label="Photo of an accountant in a suit reviewing a tax form on a clipboard beside a calculator"></div>

  <header class="brand-header">
    <span class="brand-mark"></span>
    <p class="brand-name">Harbourline<br>Accounting &amp; Taxation</p>
  </header>

  <svg class="headline-panel" viewBox="0 0 400 121" aria-hidden="true">
    <path d="M0 0H355C378 0 386 20 381 40C376 60 362 70 362 90C362 110 376 121 396 121H0Z" fill="var(--charcoal)"/>
  </svg>
  <h1 class="headline">Harbourline <span class="accent">Accounting</span><br><span class="accent">&amp; Taxation Your</span><br>Local Tax Accountant</h1>

  <h2 class="services-title">We Offer <strong>Services:</strong></h2>
  <div class="title-rule"></div>

  <div class="service" style="left:32px;top:668px;">
    <span class="service-icon"><svg viewBox="0 0 26 26" fill="none" stroke="#fff" stroke-width="1.5"><rect x="6" y="3" width="14" height="19" rx="1.5"/><path d="M9 8h8M9 11h8M9 14h5"/><rect x="4" y="16" width="12" height="5" rx="1" fill="var(--orange)"/></svg></span>
    <span class="service-label" style="margin-left:6px;">Individual &amp; Company Tax Returns</span>
  </div>
  <div class="service" style="left:32px;top:722px;">
    <span class="service-icon"><svg viewBox="0 0 26 26" fill="none" stroke="#fff" stroke-width="1.5"><path d="M13 3l5 2v4c0 3-2 5-5 6-3-1-5-3-5-6V5z"/><path d="M3 17l5-2 5 3 5-3 5 2M8 20l3 2M12 20l3 2"/></svg></span>
    <span class="service-label" style="margin-left:6px;">Company &amp; Trust formation</span>
  </div>
  <div class="service" style="left:32px;top:780px;">
    <span class="service-icon"><svg viewBox="0 0 26 26" fill="none" stroke="#fff" stroke-width="1.5"><circle cx="10" cy="7" r="3"/><path d="M5 15c0-3 2-4 5-4s5 1 5 4"/><rect x="16" y="3" width="6" height="5"/><path d="M4 16h18M6 16v7M20 16v7"/></svg></span>
    <span class="service-label" style="margin-left:6px;">Business Advisory</span>
  </div>
  <div class="service" style="left:308px;top:780px;">
    <span class="service-icon"><svg viewBox="0 0 26 26" fill="none" stroke="#fff" stroke-width="1.5"><path d="M8 3h10l4 4v16H8z"/><path d="M12 10h7M12 13h7"/><rect x="3" y="12" width="9" height="11" rx="1" fill="var(--orange)"/><path d="M5 16h2M9 16h1M5 19h2M9 19h1"/></svg></span>
    <span class="service-label" style="margin-left:5px;">Bookkeeping</span>
  </div>
  <div class="service" style="left:32px;top:837px;">
    <span class="service-icon"><svg viewBox="0 0 26 26" fill="none" stroke="#fff" stroke-width="1.5"><path d="M8 23v-4c-3-2-4-5-4-8 0-5 4-8 9-8s8 3 8 7l2 4h-2v3c0 1-1 2-2 2h-3v4"/><circle cx="13" cy="10" r="3"/></svg></span>
    <span class="service-label" style="margin-left:6px;">BAS &amp; IAS</span>
  </div>
  <div class="service" style="left:213px;top:837px;">
    <span class="service-icon"><svg viewBox="0 0 26 26" fill="none" stroke="#fff" stroke-width="1.5"><rect x="8" y="6" width="10" height="14" rx="1" transform="rotate(-30 13 13)"/><circle cx="13" cy="13" r="2"/><path d="M2 8l4-3 3 2M24 18l-4 3-3-2"/></svg></span>
    <span class="service-label" style="margin-left:12px;">Payroll</span>
  </div>
  <div class="service" style="left:358px;top:837px;">
    <span class="service-icon"><svg viewBox="0 0 26 26" fill="none" stroke="#fff" stroke-width="1.5"><path d="M5 3h12l3 3v11"/><path d="M5 3v20h11"/><path d="M8 7l3 3M11 7l-3 3M8 13h8M8 16h6"/><circle cx="20" cy="20" r="3.5"/><path d="M18.5 18.5l3 3M21.5 18.5l-3 3"/></svg></span>
    <span class="service-label" style="margin-left:11px;">TPAR</span>
  </div>

  <section class="contact-band">
    <div class="contact-item" style="left:26px;">
      <span class="contact-icon"><svg width="16" height="12" viewBox="0 0 16 12" fill="none" stroke="#fff" stroke-width="1.3"><rect x="1" y="1" width="14" height="10"/><path d="M1 1l7 6 7-6M1 11l5-5M15 11l-5-5"/></svg></span>
      <span>kolvend@hbatx.com.au</span>
    </div>
    <div class="contact-item" style="left:252px;">
      <span class="contact-icon"><svg width="12" height="16" viewBox="0 0 12 16" fill="none" stroke="#fff" stroke-width="1.4"><path d="M6 15C3 11 1 8.5 1 6a5 5 0 0 1 10 0c0 2.5-2 5-5 9z"/><circle cx="6" cy="6" r="2"/></svg></span>
      <span>9 Marlo Place, Wattle Bend</span>
    </div>
  </section>

  <section class="abn-band">
    <span class="rule"></span>
    <span><b>ABN:</b> 37 481 259 604</span>
    <span class="rule"></span>
  </section>

  <svg class="call-icon" viewBox="0 0 86 86" aria-hidden="true">
    <g transform="translate(0 10) scale(3)">
      <path d="M6.6 10.8c1.4 2.8 3.8 5.1 6.6 6.6l2.2-2.2c.3-.3.7-.4 1-.2 1.1.4 2.3.6 3.6.6.6 0 1 .4 1 1V20c0 .6-.4 1-1 1C10.6 21 3 13.4 3 4c0-.6.4-1 1-1h3.5c.6 0 1 .4 1 1 0 1.3.2 2.5.6 3.6.1.3 0 .7-.2 1L6.6 10.8z" fill="var(--orange)"/>
    </g>
    <g fill="none" stroke="var(--charcoal)" stroke-width="5" stroke-linecap="round">
      <path d="M48 30a10 10 0 0 1 10 10"/>
      <path d="M48 18a22 22 0 0 1 22 22"/>
      <path d="M48 6a34 34 0 0 1 34 34"/>
    </g>
  </svg>
  <p class="call-lead">BOOK YOUR APPOINTMENT</p>
  <p class="call-number">0419 786 205</p>
</main>
</body>
</html>
```